morvalo
sehr schöne Umsetzung. sehr schnelle freundliche und professionelle Zusammenarbeit. Gerne wieder.
Zielgruppe
Wir sind Versandhändler aus dem Bereich Büro Basteln und Schule und verkaufen neben Handelsware aus diesem Bereich auch viele eigene selbst gestaltete Artikel unter unserem Firmennamen morvalo
Aufgabenstellung
Gestaltung eines Kindergartenfreundebuches mit dem Thema Einhorn. Außenseite und Inntenteil.
Als Hardcover Buch Hochformat A5 - Titel Meine Kindergartenfreunde oder Mein Kindergarten Freundebuch.
Es geht um das Außendesign ( Vorder und Rückseite und die Inhaltsseiten ( 2 Seiten) wobei diese sich ja größtenteils immer wieder wiederholen.
Je kann man mit den Farben variieren.
Wir haben bereits Freundebücher im Sortiment
Diese sind aber eher für etwas ältere Kinder. Anbei finden Sie ein Beispiel der Druckdatei.
Das gesamte Buch hat später 88 Seiten.
Diese Serie beginnend mit dem Motiv Einhorn sollte da sowohl außen als auch innen deutlich kindlicher sein.
Daher können auch die Inhalte etwas auf Kindergarten angepasst werden
Anbei sende ich als Beispiel unsere Druckdatei von einem bestehenden Freundebuch aus unserem Sortiment
und ein Link zu einem gut umgesetzten Beispiel eines Kindergarten Freundebuchs
Das sollte nicht kopiert werden kann aber sehr gut als Muster dienen
https://www.buecherkiste-versand.de/produkt/sonnenwiese-kita-album/7741
Das Design darf nicht zu überladen sein.

```html
<!DOCTYPE html>
<html lang="de">
<head>
<meta charset="utf-8">
<title>Mein Kindergarten Freundebuch</title>
<link href="https://fonts.googleapis.com/css2?family=Mali:wght@500;600&family=Patrick+Hand&display=swap" rel="stylesheet">
<style>
:root{
  --bg:#ffffff;
  --ink:#3a3340;
  --teal:#9ccfd3;
  --lemon:#f6f3b4;
  --rose:#e8bedb;
  --green-page:#d8e8a8;
  --lilac-page:#e6dcef;
  --dash:#6b3fa0;
  --dash-soft:#9a9a9a;
  --field:#fbfaf7;
  --title-teal:#49b2c6;
  --title-purple:#7b2c98;
  --title-magenta:#b1267a;
  --cover-dash:#b1267a;
  --cloud:#fdf8e4;
  --art-warm:#efe3d2;
  --art-gold:#e6c25a;
}
*{box-sizing:border-box;margin:0;padding:0}
html,body{width:862px;height:1200px;overflow:hidden;background:var(--bg)}
body{position:relative;font-family:"Patrick Hand",cursive;color:var(--ink)}

/* ---------- spreads & pages ---------- */
.spread{position:absolute;width:510px;height:385px;display:flex;box-shadow:0 4px 14px rgba(0,0,0,.18);transform-origin:0 0}
.spread--green{left:330px;top:45px;transform:scale(.95);background:var(--green-page)}
.spread--lilac{left:43px;top:775px;background:var(--lilac-page)}
.page{position:relative;width:255px;height:385px;overflow:hidden}
.page + .page{border-left:1px solid rgba(0,0,0,.12)}
.sheet{position:absolute;left:465px;top:470px;width:370px;height:475px;
  background:linear-gradient(180deg,var(--teal) 0%,var(--lemon) 50%,var(--rose) 100%);
  box-shadow:0 4px 14px rgba(0,0,0,.18);overflow:hidden}
.sheet .page{position:absolute;left:28px;top:0;transform:scale(1.23);transform-origin:0 0}

.label{position:absolute;font-size:8.5px;line-height:1.1;white-space:nowrap}
.note{position:absolute;font-size:7.5px;line-height:1.15;white-space:nowrap}
.field{position:absolute;background:var(--field);border:1px dashed var(--dash-soft);border-radius:11px}
.spread--lilac .field,.sheet .field{border-color:var(--dash)}
.photo{position:absolute;left:14px;top:30px;width:95px;height:110px;background:#fff;
  box-shadow:0 1px 4px rgba(0,0,0,.25);border:1px dashed var(--dash)}
.art{position:absolute;border-radius:40%;background:radial-gradient(circle,var(--art-warm) 0%,rgba(239,227,210,.4) 70%,transparent 100%)}

/* ---------- cover ---------- */
.cover{position:absolute;left:25px;top:140px;width:450px;height:600px;
  background:linear-gradient(180deg,var(--teal) 0%,var(--lemon) 48%,var(--rose) 100%);
  box-shadow:0 6px 18px rgba(0,0,0,.22)}
.cover__frame{position:absolute;inset:26px;border:1.5px dashed var(--cover-dash)}
.cover__bunting{position:absolute;left:60px;top:36px;width:320px;height:70px;
  background:linear-gradient(180deg,rgba(230,194,90,.85),rgba(230,194,90,.2));border-radius:6px}
.cover__cloud{position:absolute;left:62px;top:90px;width:320px;height:165px;background:var(--cloud);border-radius:90px;box-shadow:0 0 18px rgba(255,255,255,.6)}
.cover__title{position:absolute;left:72px;top:108px;font-family:"Mali",cursive;font-weight:600;line-height:1}
.cover__title span{display:block}
.t-mein{color:var(--title-teal);font-size:48px;margin-left:22px}
.t-kg{color:var(--title-purple);font-size:46px;margin-left:8px}
.t-fb{color:var(--title-magenta);font-size:50px;margin-left:48px}
.cover__art{position:absolute;left:70px;top:270px;width:330px;height:290px;border-radius:24px;
  background:radial-gradient(ellipse at 50% 45%,#fffaf0 0%,#d9eef0 45%,rgba(201,74,160,.25) 80%,transparent 100%)}
</style>
</head>
<body>

<!-- green spread -->
<section class="spread spread--green">
  <div class="page">
    <div class="photo"></div>
    <p class="label" style="left:120px;top:30px">Mein Name:</p>
    <div class="field" style="left:120px;top:42px;width:112px;height:22px"></div>
    <p class="label" style="left:120px;top:72px">Manchmal heiße ich auch:</p>
    <div class="field" style="left:125px;top:84px;width:110px;height:22px"></div>
    <p class="label" style="left:120px;top:114px">Mein Geburtstag:</p>
    <div class="field" style="left:182px;top:110px;width:52px;height:22px"></div>
    <p class="note" style="left:112px;top:136px">So sehe ich zum Zeitpunkt<br>in deinem Bucheintrag aus!</p>
    <p class="label" style="left:22px;top:165px">Bleib mit mir in Kontakt!</p>
    <div class="field" style="left:20px;top:177px;width:215px;height:24px"></div>
    <p class="label" style="left:22px;top:208px">Das wünsche ich mir zur Zeit:</p>
    <div class="field" style="left:20px;top:220px;width:215px;height:24px"></div>
    <p class="label" style="left:22px;top:251px">Sowas mag ich überhaupt nicht:</p>
    <div class="field" style="left:20px;top:263px;width:215px;height:24px"></div>
    <p class="label" style="left:22px;top:295px">Wenn ich erwachsen bin, könnte ich diesen Beruf haben:</p>
    <div class="field" style="left:20px;top:308px;width:130px;height:24px"></div>
    <p class="label" style="left:160px;top:320px">... oder diesen:</p>
    <div class="field" style="left:100px;top:340px;width:135px;height:24px"></div>
  </div>
  <div class="page">
    <div class="art" role="img" aria-label="Kleines Einhorn mit Herzchen" style="left:14px;top:48px;width:50px;height:62px"></div>
    <p class="label" style="left:20px;top:30px">Mmh, das esse ich gerade am liebsten:</p>
    <div class="field" style="left:20px;top:42px;width:215px;height:22px"></div>
    <p class="label" style="left:70px;top:80px">... und diese Süßigkeiten mag ich besonders gerne:</p>
    <div class="field" style="left:20px;top:92px;width:215px;height:22px"></div>
    <p class="label" style="left:20px;top:125px">Oh, und diese Farben mag ich besonders:</p>
    <div class="field" style="left:110px;top:137px;width:125px;height:22px"></div>
    <p class="label" style="left:30px;top:170px">Könnte ich mich in ein Tier verwandeln,</p>
    <div class="field" style="left:15px;top:182px;width:130px;height:24px"></div>
    <p class="label" style="left:145px;top:190px">dann will ich das sein!</p>
    <div class="art" role="img" aria-label="Sitzendes Einhorn im Sonnenschein" style="left:182px;top:198px;width:58px;height:58px"></div>
    <p class="label" style="left:20px;top:222px">Diese Superkräfte zu haben wäre toll:</p>
    <div class="field" style="left:20px;top:234px;width:125px;height:24px"></div>
    <p class="label" style="left:158px;top:250px">Das spiele ich gerne:</p>
    <div class="field" style="left:110px;top:262px;width:125px;height:24px"></div>
    <p class="label" style="left:15px;top:292px">Meine aktuell liebste Fernsehsendung:</p>
    <div class="field" style="left:15px;top:304px;width:125px;height:24px"></div>
    <p class="label" style="left:150px;top:335px">Hobbies habe ich auch:</p>
    <div class="field" style="left:15px;top:347px;width:225px;height:24px"></div>
  </div>
</section>

<!-- cover -->
<section class="cover">
  <div class="cover__frame"></div>
  <div class="cover__bunting" role="img" aria-label="Goldene Wimpelkette"></div>
  <div class="cover__cloud"></div>
  <h1 class="cover__title">
    <span class="t-mein">Mein</span>
    <span class="t-kg">Kindergarten</span>
    <span class="t-fb">Freundebuch</span>
  </h1>
  <div class="cover__art" role="img" aria-label="Zwei Einhörner im hellblauen Sessel mit Freundebuch, Sterne, Luftballon und Konfettipunkte"></div>
</section>

<!-- single gradient page -->
<section class="sheet">
  <div class="page">
    <div class="art" role="img" aria-label="Kleines Einhorn mit Herzchen" style="left:14px;top:48px;width:50px;height:62px"></div>
    <p class="label" style="left:20px;top:30px">Mmh, das esse ich gerade am liebsten:</p>
    <div class="field" style="left:20px;top:42px;width:215px;height:22px"></div>
    <p class="label" style="left:70px;top:80px">... und diese Süßigkeiten mag ich besonders gerne:</p>
    <div class="field" style="left:20px;top:92px;width:215px;height:22px"></div>
    <p class="label" style="left:20px;top:125px">Oh, und diese Farben mag ich sehr:</p>
    <div class="field" style="left:110px;top:137px;width:125px;height:22px"></div>
    <p class="label" style="left:30px;top:170px">Könnte ich mich in ein Tier verwandeln,</p>
    <div class="field" style="left:15px;top:182px;width:130px;height:24px"></div>
    <p class="label" style="left:145px;top:190px">dann will ich das sein!</p>
    <div class="art" role="img" aria-label="Liegendes Einhorn im Sonnenschein" style="left:182px;top:198px;width:58px;height:58px"></div>
    <p class="label" style="left:20px;top:222px">Diese Superkräfte zu haben wäre toll:</p>
    <div class="field" style="left:20px;top:234px;width:125px;height:24px"></div>
    <p class="label" style="left:158px;top:250px">Das spiele ich gerne:</p>
    <div class="field" style="left:110px;top:262px;width:125px;height:24px"></div>
    <p class="label" style="left:15px;top:292px">Meine aktuell liebste Fernsehsendung:</p>
    <div class="field" style="left:15px;top:304px;width:125px;height:24px"></div>
    <p class="label" style="left:150px;top:335px">Hobbies habe ich auch:</p>
    <div class="field" style="left:15px;top:347px;width:225px;height:24px"></div>
  </div>
</section>

<!-- lilac spread -->
<section class="spread spread--lilac">
  <div class="page">
    <div class="photo"></div>
    <p class="label" style="left:120px;top:30px">Mein Name:</p>
    <div class="field" style="left:120px;top:42px;width:112px;height:22px"></div>
    <p class="label" style="left:120px;top:72px">Manchmal heiße ich auch:</p>
    <div class="field" style="left:125px;top:84px;width:110px;height:22px"></div>
    <p class="label" style="left:120px;top:114px">Mein Geburtstag:</p>
    <div class="field" style="left:182px;top:110px;width:52px;height:22px"></div>
    <p class="note" style="left:112px;top:136px">So sehe ich zum Zeitpunkt<br>in deinem Bucheintrag aus!</p>
    <p class="label" style="left:22px;top:165px">Bleib mit mir in Kontakt!</p>
    <div class="field" style="left:20px;top:177px;width:215px;height:24px"></div>
    <div class="art" role="img" aria-label="Sitzendes Einhorn mit rosa Mähne" style="left:196px;top:168px;width:50px;height:70px"></div>
    <p class="label" style="left:22px;top:208px">Das wünsche ich mir zur Zeit:</p>
    <div class="field" style="left:20px;top:220px;width:180px;height:24px"></div>
    <p class="label" style="left:22px;top:251px">Sowas mag ich überhaupt nicht:</p>
    <div class="field" style="left:20px;top:263px;width:215px;height:24px"></div>
    <p class="label" style="left:22px;top:295px">Wenn ich erwachsen bin, könnte ich diesen Beruf haben:</p>
    <div class="field" style="left:20px;top:308px;width:130px;height:24px"></div>
    <div class="art" role="img" aria-label="Zwei grüne Luftballons" style="left:12px;top:318px;width:50px;height:60px;background:radial-gradient(circle,rgba(160,210,170,.8),transparent 70%)"></div>
    <p class="label" style="left:160px;top:320px">... oder diesen:</p>
    <div class="field" style="left:100px;top:340px;width:135px;height:24px"></div>
  </div>
  <div class="page">
    <div class="art" role="img" aria-label="Kleines Einhorn mit Herzchen" style="left:14px;top:48px;width:50px;height:62px"></div>
    <p class="label" style="left:20px;top:30px">Mmh, das esse ich gerade am liebsten:</p>
    <div class="field" style="left:20px;top:42px;width:215px;height:22px"></div>
    <p class="label" style="left:70px;top:80px">... und diese Süßigkeiten mag ich besonders gerne:</p>
    <div class="field" style="left:20px;top:92px;width:215px;height:22px"></div>
    <p class="label" style="left:20px;top:125px">Oh, und diese Farben mag ich besonders:</p>
    <div class="field" style="left:110px;top:137px;width:125px;height:22px"></div>
    <p class="label" style="left:30px;top:170px">Könnte ich mich in ein Tier verwandeln,</p>
    <div class="field" style="left:15px;top:182px;width:130px;height:24px"></div>
    <p class="label" style="left:145px;top:190px">dann will ich das sein!</p>
    <div class="art" role="img" aria-label="Liegendes Einhorn im Sonnenschein" style="left:182px;top:198px;width:58px;height:58px"></div>
    <p class="label" style="left:20px;top:222px">Diese Superkräfte zu haben wäre toll:</p>
    <div class="field" style="left:20px;top:234px;width:125px;height:24px"></div>
    <p class="label" style="left:158px;top:250px">Das spiele ich gerne:</p>
    <div class="field" style="left:110px;top:262px;width:125px;height:24px"></div>
    <p class="label" style="left:15px;top:292px">Meine aktuell liebste Fernsehsendung:</p>
    <div class="field" style="left:15px;top:304px;width:125px;height:24px"></div>
    <p class="label" style="left:150px;top:335px">Hobbies habe ich auch:</p>
    <div class="field" style="left:15px;top:347px;width:225px;height:24px"></div>
  </div>
</section>

</body>
</html>
```